Display Ad for Local Publication

We have never advertised before but now I would like to have an ad running in our local, community magazine. Our business is Cedar Hollow Mini Storage located in Kestrel Bay, WA. PL is a small community (+/-2,500 people located across the Puget Sound from Seattle. The monthly magazine, The Tidings, covers all kinds of local news and activities and carries a number of ads from local businesses. Our is the only mini storage in Port Ludlow. We have enclosed storage units of various sizes and outdoor parking spaces for boats, trailers and RVs. I am enclosing a business card and the size requirements for Tidings advertisements. I want to develop a 1/8 page ad.

```html
<!DOCTYPE html>
<html lang="en">
<head>
<meta charset="utf-8">
<title>Cedar Hollow Mini Storage – Display Ad</title>
<link href="https://fonts.googleapis.com/css2?family=Arvo:wght@700&family=Poppins:wght@500;600&display=swap" rel="stylesheet">
<style>
  :root {
    --navy: #1f2259;
    --navy-deep: #1a1c4e;
    --blue: #2383c0;
    --sky: #2f8fd6;
    --green: #33cc5e;
    --white: #ffffff;
    --ink: #1c1c24;
    --stage: #e9eaee;
  }
  * { margin: 0; padding: 0; box-sizing: border-box; }
  html, body { width: 1200px; height: 953px; overflow: hidden; background: var(--stage); }
  .ad {
    position: absolute; left: 40px; top: 129px;
    width: 1259px; height: 780px;
    transform: scale(0.8896); transform-origin: 0 0;
    overflow: hidden; background: var(--white);
  }
  .hero {
    position: absolute; left: 0; top: 0; width: 1259px; height: 473px;
    background: linear-gradient(120deg, var(--navy-deep), var(--navy) 60%, #232766);
  }
  .photo-frame {
    position: absolute; left: 57px; top: 59px; width: 675px; height: 395px;
    border: 2px solid var(--sky); border-radius: 12px 48px 48px 12px; padding: 6px;
  }
  .photo {
    width: 100%; height: 100%; border-radius: 6px 40px 40px 6px;
    background: linear-gradient(90deg, #c9ccd2, #eef0f3 35%, #d9dbe0 55%, #f3f4f6 75%, #c4c7cd);
  }
  .title {
    position: absolute; left: 774px; top: 54px;
    font: 700 58px/62px "Arvo", serif; color: var(--white);
  }
  .title .accent { color: var(--sky); }
  .perks { position: absolute; left: 777px; top: 270px; list-style: none; }
  .perks li {
    display: flex; align-items: center; gap: 9px;
    width: 219px; height: 46px; margin-bottom: 7px; padding-left: 12px;
    background: var(--green); border-radius: 0 23px 23px 0;
    font: 600 26px "Poppins", sans-serif; color: var(--navy-deep);
  }
  .offer {
    position: absolute; left: 0; top: 473px; width: 731px; height: 145px;
    background: var(--green); padding: 30px 0 0 58px;
    font: 700 35px/47px "Arvo", serif; color: var(--navy-deep);
  }
  .quick {
    position: absolute; left: 58px; top: 650px; display: flex; align-items: center; gap: 12px;
    font: 600 34px "Poppins", sans-serif; color: var(--ink);
  }
  .quick .gap { width: 8px; }
  .contact {
    position: absolute; left: 733px; top: 473px; width: 526px; height: 307px; background: var(--blue);
  }
  .contact-tab {
    position: absolute; left: 0; top: 14px; width: 182px; height: 73px;
    background: var(--navy-deep); border-radius: 0 26px 26px 0;
    font: 700 29px/73px "Arvo", serif; color: var(--white); text-align: center;
  }
  .person { position: absolute; left: 197px; top: 14px; color: var(--white); }
  .person .name { font: 700 35px/44px "Arvo", serif; }
  .person .role { font: 600 22px/26px "Poppins", sans-serif; }
  .details { position: absolute; left: 36px; top: 108px; list-style: none; color: var(--white);
    font: 500 23px/29px "Poppins", sans-serif; }
  .details li { display: flex; gap: 9px; margin-bottom: 6px; }
  .details svg { flex: none; margin-top: 3px; }
</style>
</head>
<body>
<div class="ad">
  <section class="hero">
    <div class="photo-frame">
      <div class="photo" role="img" aria-label="Bright indoor corridor lined with white roll-up storage unit doors"></div>
    </div>
    <h1 class="title">Cedar<br>Hollow Mini<br><span class="accent">Storage</span></h1>
    <ul class="perks">
      <li><svg width="18" height="18" viewBox="0 0 18 18"><circle cx="9" cy="9" r="9" fill="#fff"/><path d="M5 9.3l2.6 2.5L13 6.5" stroke="#33cc5e" stroke-width="2.2" fill="none"/></svg>Secure</li>
      <li><svg width="18" height="18" viewBox="0 0 18 18"><circle cx="9" cy="9" r="9" fill="#fff"/><path d="M5 9.3l2.6 2.5L13 6.5" stroke="#33cc5e" stroke-width="2.2" fill="none"/></svg>Local</li>
      <li><svg width="18" height="18" viewBox="0 0 18 18"><circle cx="9" cy="9" r="9" fill="#fff"/><path d="M5 9.3l2.6 2.5L13 6.5" stroke="#33cc5e" stroke-width="2.2" fill="none"/></svg>Convenient</li>
    </ul>
  </section>

  <div class="offer">Indoor Units +<br>Outdoor RV/Boat Parking</div>

  <div class="quick">
    <svg width="38" height="38" viewBox="0 0 38 38"><circle cx="19" cy="19" r="19" fill="#2383c0"/><path d="M13 11c1-1 2-1 3 0l2 3c.5 1 0 2-1 2.5 1 2.5 3 4.5 5.5 5.5.5-1 1.5-1.5 2.5-1l3 2c1 1 1 2 0 3-2 2-4 2-7 0-3-2-6-5-8-8-2-3-2-5 0-7z" fill="#fff"/></svg>
    <span>360 555 0147</span>
    <span class="gap"></span>
    <svg width="38" height="38" viewBox="0 0 38 38"><circle cx="19" cy="19" r="19" fill="#2383c0"/><path d="M19 9a7 7 0 0 0-7 7c0 5 7 12 7 12s7-7 7-12a7 7 0 0 0-7-7z" fill="#fff"/><circle cx="19" cy="16" r="2.6" fill="#2383c0"/></svg>
    <span>Kestrel Bay, WA</span>
  </div>

  <section class="contact">
    <div class="contact-tab">Contact</div>
    <div class="person">
      <div class="name">Daniel Ferris</div>
      <div class="role">Proprietor</div>
    </div>
    <ul class="details">
      <li><svg width="26" height="26" viewBox="0 0 26 26"><circle cx="13" cy="13" r="13" fill="#33cc5e"/><path d="M13 6a4.5 4.5 0 0 0-4.5 4.5C8.5 14 13 19 13 19s4.5-5 4.5-8.5A4.5 4.5 0 0 0 13 6z" fill="#fff"/><circle cx="13" cy="10.5" r="1.7" fill="#33cc5e"/></svg><span>118 Harbor View Rd PO Box 4410<br>Kestrel Bay WA 98000</span></li>
      <li><svg width="26" height="26" viewBox="0 0 26 26"><circle cx="13" cy="13" r="13" fill="#33cc5e"/><path d="M9 7.5c.7-.7 1.4-.7 2 0l1.4 2c.3.7 0 1.4-.7 1.7.7 1.7 2 3 3.7 3.7.3-.7 1-1 1.7-.7l2 1.4c.7.7.7 1.4 0 2-1.4 1.4-2.8 1.4-4.8 0-2-1.4-4-3.4-5.4-5.4-1.4-2-1.4-3.4.1-4.7z" fill="#fff"/></svg><span>360 555 0192</span></li>
      <li><svg width="26" height="26" viewBox="0 0 26 26"><circle cx="13" cy="13" r="13" fill="#33cc5e"/><rect x="7" y="8.5" width="12" height="9" rx="1" fill="#fff"/><path d="M7.5 9l5.5 4.5L18.5 9" stroke="#33cc5e" stroke-width="1.4" fill="none"/></svg><span>chministorage@example.com</span></li>
    </ul>
  </section>
</div>
</body>
</html>
```